British Columbia Day banner showcasing 20% off site

Banner graphic promoting our BC Day sale
Size: 1800 x 1000
- flag has been uploaded for inspiration
- examples from other companies and their sale banners have been uploaded for inspiration.
- product images can be found at www.kelvoraleaf.com, please use a variety of different products in this banner

Target Market(s)

19+

Industry/Entity Type

Cannabis

Requirements
Must have
• Phrases:
- “Celebrate BC Day with BC bud and companies”
- “20% off site wide sale*"
- Underneath phrase the date of sale “July 30th - August 3rd”
- In tiny print “*excludes all sale and bundled items”
- MUST BE 1800 X1000
Nice to have
• - images of the products or bud we carry which can be found at www.kelvoraleaf.com
- bold
Should not have
• - company logo

```html
<!DOCTYPE html>
<html lang="en">
<head>
<meta charset="utf-8">
<title>BC Day Sale Banner</title>
<link rel="stylesheet" href="https://fonts.googleapis.com/css2?family=Ultra&family=Quicksand:wght@300;400;600&display=swap">
<style>
  :root {
    --page-top: #1c3a44;
    --page-mid: #2c3338;
    --page-bottom: #0d0d0d;
    --panel-center: #37a9c8;
    --panel-mid: #2a8aa6;
    --panel-edge: #1c6479;
    --frame-line: #7fe3f5;
    --text-white: #f4fbfc;
    --bud-light: #7da356;
    --bud-mid: #4f7f4c;
    --bud-dark: #2c5a4e;
    --tin-face: #4a3f42;
    --tin-rim: #2a2628;
    --box-face: #2f7485;
    --box-line: #1f5564;
    --gummy-green: #78b23c;
    --brand-ink: #15191b;
  }
  * { margin: 0; padding: 0; box-sizing: border-box; }
  html, body { width: 1200px; height: 720px; overflow: hidden; }
  body {
    position: relative;
    background: linear-gradient(180deg, var(--page-top) 0%, var(--page-mid) 55%, var(--page-bottom) 100%);
    font-family: "Quicksand", sans-serif;
  }
  .banner {
    position: absolute;
    left: 109px; top: 27px;
    width: 982px; height: 545px;
    overflow: hidden;
    background: radial-gradient(ellipse at 50% 48%, var(--panel-center) 0%, var(--panel-mid) 55%, var(--panel-edge) 100%);
  }
  .banner__frame {
    position: absolute;
    left: 11px; top: 6px; right: 11px; bottom: 6px;
    border: 2px solid var(--frame-line);
    opacity: .85;
  }

  /* product photo areas */
  .photo { position: absolute; }
  .photo--bud {
    background: radial-gradient(ellipse at 45% 40%, var(--bud-light) 0%, var(--bud-mid) 45%, var(--bud-dark) 100%);
    clip-path: polygon(30% 0%, 62% 4%, 88% 18%, 100% 45%, 92% 76%, 70% 96%, 40% 100%, 14% 86%, 0% 58%, 6% 26%);
    opacity: .8;
  }
  .photo--tin {
    border-radius: 50%;
    background: radial-gradient(circle at 50% 50%, var(--tin-face) 0%, var(--tin-face) 62%, var(--tin-rim) 64%, #3d4448 100%);
    opacity: .8;
  }
  .photo--box {
    border: 2px solid var(--box-line);
    background: linear-gradient(160deg, var(--box-face), #276576);
    opacity: .7;
  }
  .photo--gummy {
    border-radius: 50% 45% 50% 42%;
    background: radial-gradient(circle at 40% 35%, #9bd15a 0%, var(--gummy-green) 60%, #4f8a2c 100%);
  }
  .photo--gummies {
    border-radius: 10px;
    background: linear-gradient(100deg, #8ec6c9 0%, #a6d37a 25%, #d7b784 45%, #9fd2d4 65%, #c9868a 80%, #b7cfd2 100%);
    opacity: .6;
  }

  .headline {
    position: absolute;
    left: 22px; right: 20px; top: 19px;
    text-align: center;
    font-family: "Ultra", "Rockwell", serif;
    font-weight: 400;
    font-size: 48px;
    line-height: 67px;
    letter-spacing: 4px;
    word-spacing: 8px;
    color: var(--text-white);
    text-shadow: 0 2px 3px rgba(10, 40, 50, .35);
  }
  .sale {
    position: absolute;
    left: 0; right: 0; top: 266px;
    text-align: center;
    font-weight: 300;
    font-size: 64px;
    line-height: 80px;
    color: var(--text-white);
  }
  .dates {
    position: absolute;
    right: 36px; top: 362px;
    font-weight: 300;
    font-size: 37px;
    line-height: 44px;
    color: var(--text-white);
  }
  .fine-print {
    position: absolute;
    right: 24px; top: 515px;
    font-weight: 300;
    font-size: 17px;
    line-height: 22px;
    color: var(--text-white);
  }
  .brand {
    position: absolute;
    left: 0; right: 0; top: 470px;
    display: flex; justify-content: center; align-items: center; gap: 8px;
    font-weight: 600;
    font-size: 20px;
    color: var(--brand-ink);
  }
  .brand__mark { width: 16px; height: 16px; background: var(--brand-ink); }
</style>
</head>
<body>
  <section class="banner">
    <div class="photo photo--bud" role="img" aria-label="Cannabis bud, top left" style="left:0;top:-8px;width:182px;height:130px"></div>
    <div class="photo photo--bud" role="img" aria-label="Cannabis bud, top" style="left:312px;top:-14px;width:112px;height:48px"></div>
    <div class="photo photo--bud" role="img" aria-label="Large cannabis bud, centre" style="left:412px;top:64px;width:180px;height:216px"></div>
    <div class="photo photo--bud" role="img" aria-label="Cannabis bud, left" style="left:153px;top:133px;width:113px;height:140px"></div>
    <div class="photo photo--bud" role="img" aria-label="Cannabis bud, top right" style="left:706px;top:-4px;width:246px;height:214px"></div>
    <div class="photo photo--bud" role="img" aria-label="Cannabis bud, right" style="left:846px;top:246px;width:150px;height:118px"></div>
    <div class="photo photo--bud" role="img" aria-label="Cannabis bud, bottom" style="left:266px;top:462px;width:108px;height:100px"></div>
    <div class="photo photo--tin" role="img" aria-label="Strawberry gummy tin" style="left:-18px;top:176px;width:118px;height:136px"></div>
    <div class="photo photo--box" role="img" aria-label="Edible product package" style="left:45px;top:380px;width:106px;height:130px"></div>
    <div class="photo photo--gummy" role="img" aria-label="Green gummy" style="left:172px;top:396px;width:38px;height:42px"></div>
    <div class="photo photo--gummy" role="img" aria-label="Green gummy" style="left:157px;top:450px;width:36px;height:42px"></div>
    <div class="photo photo--gummies" role="img" aria-label="Assorted gummy cubes" style="left:706px;top:414px;width:224px;height:90px"></div>

    <div class="banner__frame"></div>

    <h1 class="headline">Celebrate BC Day with BC bud<br>and companies</h1>
    <p class="sale">20% off site wide sale</p>
    <p class="dates">July 30th - August 3rd</p>
    <div class="brand"><span class="brand__mark"></span><span>Kelvora Leaf</span></div>
    <p class="fine-print">*excludes all sale and bundled items</p>
  </section>
</body>
</html>
```